I want to redesign the Tallvo corporate website

Brookhill Agro Limited (Tallvo) is a Nigerian integrated agribusiness and premium food company operating across agriculture, food processing and nationwide FMCG distribution.
We are redesigning our corporate website to reflect our evolution into a modern, premium food company capable of serving institutional buyers, distributors, retailers, investors and consumers. The new website should feel comparable to the websites of leading global food brands — not a typical agricultural website.

Target Market(s)

Nigeria / Africa

Industry/Entity Type

FMCG

Coding

Number of Pages Required

5+ page

Colors

Designer to choose colors to be used in the design.

Requirements
Must have
• The website must communicate the following attributes consistently across every page, in both design and language. Premium Quality of finish signals quality of product , Clean Uncluttered layouts, disciplined use of elements ,Modern Current design language, not dated conventions ,Innovative and Forward-looking, technology-enabled , Sustainable Responsible practice made visible Nigerian with global standards, Proudly local in origin, international in execution
Nice to have
• Lots of white space , Fast loading, Premium photography,Mobile-first,Elegant typography,Minimal clutter, Rounded elements,High-end corporate feel, Smooth curved section transitions, Soft shadows
Should not have
• The new website should feel comparable to the websites of leading global food brands — not a typical agricultural website. Also do not copy the business profile as website , its is just a guide !

```html
<!DOCTYPE html>
<html lang="en">
<head>
<meta charset="utf-8">
<title>Tallvo — Integrated Agriculture. Nourishing Lives.</title>
<link href="https://fonts.googleapis.com/css2?family=Outfit:wght@300;400;500;600&display=swap" rel="stylesheet">
<style>
:root{
  --green:#3f8f1f;
  --green-bright:#4fa323;
  --green-dark:#1f5717;
  --green-deep:#1d4f16;
  --ink:#111511;
  --muted:#3c403b;
  --panel:#f4f5ef;
  --line:#e4e6df;
  --white:#ffffff;
}
*{box-sizing:border-box;margin:0;padding:0}
html,body{width:1200px;height:2720px;overflow:hidden;background:var(--white)}
body{position:relative;font-family:"Outfit",sans-serif;color:var(--ink)}
.abs{position:absolute}
.btn{position:absolute;display:flex;align-items:center;justify-content:center;border-radius:999px;font-size:12.5px;font-weight:500;text-decoration:none}
.btn-solid{background:var(--green-dark);color:var(--white)}
.btn-ghost{background:var(--white);color:var(--ink);border:1px solid var(--green-dark)}
.eyebrow{position:absolute;font-size:14.5px;font-weight:500;color:var(--green);text-transform:uppercase;letter-spacing:.2px}
.arrow-btn{position:absolute;width:36px;height:36px;border-radius:50%;border:1px solid #cfd3cb;background:var(--white);display:flex;align-items:center;justify-content:center}

/* header */
.site-header{position:absolute;left:0;top:0;width:1200px;height:91px;background:var(--white)}
.brand{position:absolute;left:150px;top:20px;font-size:40px;font-weight:600;color:var(--green-bright);letter-spacing:-.5px;line-height:1}
.nav{position:absolute;left:302px;top:37px;display:flex;gap:0;font-size:12px;font-weight:400}
.nav a{color:var(--ink);text-decoration:none;margin-right:24px}
.nav a.active{color:var(--green);border-bottom:1.5px solid var(--green);padding-bottom:4px}

/* hero */
.hero{position:absolute;left:0;top:91px;width:1200px;height:469px;overflow:hidden}
.hero-photo{position:absolute;inset:0;background:
  radial-gradient(ellipse at 70% 65%,#c99a52 0%,rgba(201,154,82,0) 38%),
  linear-gradient(180deg,#dfe9e6 0%,#b8cfa5 30%,#6f9a45 60%,#8a6a3e 85%,#6d4d2a 100%)}
.hero-fade{position:absolute;left:0;top:0;width:620px;height:469px;background:linear-gradient(90deg,rgba(255,255,255,.82) 0%,rgba(255,255,255,.55) 60%,rgba(255,255,255,0) 100%)}
.hero-title{position:absolute;left:150px;top:60px;font-size:45px;font-weight:500;line-height:54px;letter-spacing:-.3px}
.hero-title .accent{color:var(--green-bright)}
.hero-copy{position:absolute;left:150px;top:233px;width:290px;font-size:12px;line-height:16.5px;color:var(--ink)}
.hero-curve{position:absolute;left:0;top:0}
.dots{position:absolute;left:580px;top:442px;display:flex;gap:7px}
.dots span{width:7px;height:7px;border-radius:50%;background:var(--white)}
.dots span.on{background:var(--green-bright)}

/* about */
.tile{position:absolute;border-radius:12px}
.about-title{position:absolute;left:621px;top:676px;font-size:34px;font-weight:500;line-height:40px;letter-spacing:-.2px}
.about-copy{position:absolute;left:623px;top:766px;width:360px;font-size:11.6px;line-height:16.6px;color:var(--muted)}
.features{position:absolute;left:621px;top:848px;display:flex}
.feature{width:108px;text-align:center;font-size:12px;line-height:16px;border-right:1px solid var(--line);padding-top:2px;height:82px}
.feature:last-child{border-right:none}
.feature svg{display:block;margin:0 auto 10px}

/* products */
.products{position:absolute;left:150px;top:1074px;width:899px;height:442px;background:var(--panel);border-radius:30px}
.section-title{position:absolute;font-size:32px;font-weight:500;letter-spacing:-.2px}
.card{position:absolute;top:146px;width:203px;height:246px;background:var(--white);border:1px solid var(--line);border-radius:22px;box-shadow:0 4px 14px rgba(20,40,10,.05)}
.card-img{position:absolute;left:16px;top:16px;width:171px;height:130px;border-radius:14px}
.card h3{position:absolute;left:15px;top:160px;font-size:15.5px;font-weight:600}
.card p{position:absolute;left:15px;top:188px;width:130px;font-size:11.6px;line-height:17px;color:var(--muted)}
.card .arrow-btn{left:152px;top:187px}

/* value chain */
.chain-line{position:absolute;left:212px;top:1736px;width:774px;border-top:1px dashed #8fbf6e}
.stage{position:absolute;top:1673px;width:150px;text-align:center}
.stage .disc{width:125px;height:125px;border-radius:50%;margin:0 auto}
.stage p{margin-top:22px;font-size:15px;line-height:18px}

/* sustainability */
.sustain{position:absolute;left:150px;top:1917px;width:899px;height:246px;background:var(--green-deep);border-radius:30px;overflow:hidden}
.sustain-photo{position:absolute;left:0;top:0;width:300px;height:246px;background:linear-gradient(90deg,#2f6a22 0%,#3d7a2a 45%,rgba(29,79,22,0) 100%)}
.sustain h2{position:absolute;left:236px;top:52px;font-size:32px;font-weight:500;line-height:40px;color:var(--white)}
.sustain .copy{position:absolute;left:239px;top:139px;width:310px;font-size:11.6px;line-height:16.6px;color:#e6eee2}
.pillar{position:absolute;top:67px;width:110px;text-align:center;color:var(--white);font-size:12px;line-height:15px}
.pillar .ring{width:64px;height:64px;border-radius:50%;border:1.5px solid #7cc25a;margin:0 auto 14px;display:flex;align-items:center;justify-content:center}

/* teasers */
.teaser{position:absolute;top:2224px;width:291px;height:182px;border:1px solid var(--line);border-radius:22px;overflow:hidden;background:var(--white)}
.teaser .eyebrow{position:static;font-size:12px}
.teaser .body{position:absolute;left:15px;top:22px;width:170px}
.teaser h3{margin-top:5px;font-size:18.5px;font-weight:400;line-height:23px}
.teaser p{margin-top:6px;font-size:11.6px;line-height:17px;color:var(--muted)}
.teaser .arrow-btn{left:15px;top:131px}
.teaser-photo{position:absolute;right:0;top:0;width:150px;height:182px}

/* footer */
.site-footer{position:absolute;left:0;top:2467px;width:1200px;height:253px;background:var(--green-deep);color:var(--white)}
.footer-brand{position:absolute;left:0;width:1200px;top:48px;text-align:center;font-size:52px;font-weight:600;letter-spacing:-.5px;color:var(--white)}
.socials{position:absolute;left:530px;top:133px;display:flex;gap:17px}
.socials span{width:35px;height:35px;border-radius:50%;border:1.2px solid rgba(255,255,255,.85)}
.footer-links{position:absolute;left:0;width:1200px;top:184px;text-align:center;font-size:12px}
.footer-links a{color:var(--white);text-decoration:none;margin:0 12px}
.footer-links i{font-style:normal;opacity:.8}
.footer-rule{position:absolute;left:0;top:216px;width:1200px;border-top:1px solid rgba(255,255,255,.2)}
.copyright{position:absolute;left:0;width:1200px;top:228px;text-align:center;font-size:10px;opacity:.9}
</style>
</head>
<body>

<header class="site-header">
  <div class="brand">tallvo</div>
  <nav class="nav">
    <a class="active" href="#">Home</a><a href="#">About Us</a><a href="#">Products</a><a href="#">Our Business</a><a href="#">Sustainability</a><a href="#">Investors</a><a href="#">News &amp; Media</a><a href="#">Careers</a>
  </nav>
  <a class="btn btn-solid" href="#" style="left:934px;top:28px;width:115px;height:35px;background:#2c7d1b">Contact Us</a>
</header>

<section class="hero">
  <div class="hero-photo" role="img" aria-label="Basket of eggs, green plantains, plantain chips pack and honey jar on a wooden table before green hills"></div>
  <div class="hero-fade"></div>
  <h1 class="hero-title">Integrated<br><span class="accent">Agriculture.</span><br>Nourishing Lives.</h1>
  <p class="hero-copy">From our farms to your table - we produce premium, safe and nutritious food through innovation, quality and responsibility.</p>
  <a class="btn btn-solid" href="#" style="left:150px;top:299px;width:130px;height:35px;background:#2c7d1b">Explore Products</a>
  <a class="btn btn-ghost" href="#" style="left:293px;top:299px;width:129px;height:35px">About Tallvo</a>
  <svg class="hero-curve" width="1200" height="469" viewBox="0 0 1200 469">
    <path d="M0 372 C260 430 520 474 760 466 C940 460 1080 430 1200 392 L1200 469 L0 469 Z" fill="#ffffff"/>
    <path d="M0 362 C180 400 330 432 470 452 C390 440 200 404 0 376 Z" fill="#3f8f1f"/>
  </svg>
  <div class="dots"><span class="on"></span><span></span><span></span></div>
</section>

<section class="about">
  <div class="tile" style="left:150px;top:625px;width:213px;height:191px;background:linear-gradient(180deg,#f4f1e6 0%,#e6dccb 55%,#9a6a44 100%)" role="img" aria-label="Corporate profile cover with company headquarters building"></div>
  <div class="tile" style="left:370px;top:625px;width:211px;height:243px;background:linear-gradient(160deg,#4a3a2e 0%,#2b3550 60%,#1f2a48 100%)" role="img" aria-label="Portrait of company executive in a blue suit"></div>
  <div class="tile" style="left:150px;top:822px;width:213px;height:190px;background:linear-gradient(160deg,#6fa645 0%,#3d7a2a 60%,#2b5a1e 100%)" role="img" aria-label="Farmer holding a bunch of green plantains"></div>
  <div class="tile" style="left:370px;top:874px;width:211px;height:138px;background:linear-gradient(160deg,#e7ecef 0%,#c9d4dc 55%,#8aa6bd 100%)" role="img" aria-label="Scientist examining a sample under a microscope"></div>

  <div class="eyebrow" style="left:621px;top:653px">About Tallvo</div>
  <h2 class="about-title">Rooted in Nigeria.<br>Focused on the World.</h2>
  <p class="about-copy">Brookhill Agro Limited (Tallvo) is an integrated agribusiness and premium food company delivering high-quality products through sustainable practices, advanced technology and a commitment to people and communities.</p>
  <div class="features">
    <div class="feature"><svg width="30" height="30" viewBox="0 0 30 30" fill="none" stroke="#3f8f1f" stroke-width="1.4"><path d="M5 11 L10 4 H20 L25 11 L15 26 Z"/><path d="M5 11 H25 M10 4 L15 11 L20 4 M15 11 V26"/></svg>Premium<br>Quality</div>
    <div class="feature"><svg width="30" height="30" viewBox="0 0 30 30" fill="none" stroke="#3f8f1f" stroke-width="1.4"><circle cx="15" cy="15" r="10"/><path d="M9 18 C9 11 15 8 22 8 C22 15 18 20 11 20 M11 20 L17 13"/></svg>Sustainable<br>Practices</div>
    <div class="feature"><svg width="30" height="30" viewBox="0 0 30 30" fill="none" stroke="#3f8f1f" stroke-width="1.4"><path d="M11 15 C8 13 8 6 15 6 C22 6 22 13 19 15 V18 H11 Z"/><path d="M12 21 H18 M4 26 H11 C13 26 14 24 16 24 H20"/><path d="M15 1 V3 M7 4 L8.5 5.5 M23 4 L21.5 5.5"/></svg>Innovative<br>Solutions</div>
    <div class="feature"><svg width="30" height="30" viewBox="0 0 30 30" fill="none" stroke="#3f8f1f" stroke-width="1.4"><path d="M12 4 H18 M13 4 V13 L7 25 H23 L17 13 V4"/><path d="M9.5 20 H20.5"/><circle cx="15" cy="9" r="1"/></svg>Nourishing<br>Lives</div>
  </div>
  <a class="btn btn-solid" href="#" style="left:623px;top:950px;width:167px;height:35px;background:#2c7d1b">Learn More About Us</a>
</section>

<section class="products">
  <div class="eyebrow" style="left:22px;top:43px">Our Products</div>
  <h2 class="section-title" style="left:22px;top:71px">Good for you. good for all.</h2>
  <a class="btn btn-solid" href="#" style="left:710px;top:75px;width:167px;height:34px;background:#2c7d1b">View all products</a>

  <article class="card" style="left:22px">
    <div class="card-img" style="background:radial-gradient(ellipse at 50% 55%,#d99a63 0%,#e9c9a6 45%,#ffffff 75%)" role="img" aria-label="Bowl of brown eggs"></div>
    <h3>Premium Eggs</h3><p>Nutritious. Farm-fresh. Always trusted.</p>
    <span class="arrow-btn"><svg width="14" height="10" viewBox="0 0 14 10" fill="none" stroke="#111" stroke-width="1.3"><path d="M1 5 H12 M8 1 L12 5 L8 9"/></svg></span>
  </article>
  <article class="card" style="left:240px">
    <div class="card-img" style="background:radial-gradient(ellipse at 50% 50%,#f0b73a 0%,#f7d98a 45%,#ffffff 75%)" role="img" aria-label="Wooden bowl of plantain chips"></div>
    <h3>Plantain Chips</h3><p>Crispy. Natural Irresistibly good.</p>
    <span class="arrow-btn"><svg width="14" height="10" viewBox="0 0 14 10" fill="none" stroke="#111" stroke-width="1.3"><path d="M1 5 H12 M8 1 L12 5 L8 9"/></svg></span>
  </article>
  <article class="card" style="left:457px">
    <div class="card-img" style="background:radial-gradient(ellipse at 50% 55%,#d4761a 0%,#f0c17a 40%,#ffffff 72%)" role="img" aria-label="Jar of honey with a wooden dipper"></div>
    <h3>Pure Honey</h3><p>Pure. Natural. Uncompromised.</p>
    <span class="arrow-btn"><svg width="14" height="10" viewBox="0 0 14 10" fill="none" stroke="#111" stroke-width="1.3"><path d="M1 5 H12 M8 1 L12 5 L8 9"/></svg></span>
  </article>
  <article class="card" style="left:675px">
    <div class="card-img" style="background:radial-gradient(ellipse at 50% 50%,#5f9a2e 0%,#b7cf95 45%,#ffffff 75%)" role="img" aria-label="Product box covered with a green cloth"></div>
    <h3>Future Products</h3><p>Innovating today for a better tomorrow.</p>
    <span class="arrow-btn"><svg width="14" height="10" viewBox="0 0 14 10" fill="none" stroke="#111" stroke-width="1.3"><path d="M1 5 H12 M8 1 L12 5 L8 9"/></svg></span>
  </article>
</section>

<section class="chain">
  <div class="eyebrow" style="left:0;width:1200px;text-align:center;top:1566px">Our Business</div>
  <h2 class="section-title" style="left:0;width:1200px;text-align:center;top:1595px">An Integrated Value Chain</h2>
  <div class="chain-line"></div>
  <div class="stage" style="left:137px"><div class="disc" style="background:linear-gradient(160deg,#c9b59a,#a07a52)" role="img" aria-label="Worker inspecting chickens in a poultry house"></div><p>Poultry<br>Farming</p></div>
  <div class="stage" style="left:292px"><div class="disc" style="background:linear-gradient(160deg,#7bb04a,#3b6e22)" role="img" aria-label="Plantain bunches growing on a farm"></div><p>Plantain<br>Farming</p></div>
  <div class="stage" style="left:447px"><div class="disc" style="background:linear-gradient(160deg,#dfe6ec,#a83a3a)" role="img" aria-label="Food processing line with staff in protective wear"></div><p>Food<br>Processing</p></div>
  <div class="stage" style="left:602px"><div class="disc" style="background:linear-gradient(160deg,#c7d6c2,#5f8f3e)" role="img" aria-label="Aerial view of distribution routes across farmland"></div><p>Distribution<br>Selected Area</p></div>
  <div class="stage" style="left:757px"><div class="disc" style="background:linear-gradient(160deg,#e6ece4,#4f8a2f)" role="img" aria-label="Quality inspector checking crops with a tablet"></div><p>Quality<br>Assurance</p></div>
  <div class="stage" style="left:911px"><div class="disc" style="background:linear-gradient(160deg,#dbe4ee,#2d4a78)" role="img" aria-label="Researchers working in a laboratory"></div><p>Research<br>&amp; Innovation</p></div>
</section>

<section class="sustain">
  <div class="sustain-photo" role="img" aria-label="Lush plantain plantation"></div>
  <div class="eyebrow" style="left:237px;top:30px;color:#7cc25a">Our Business</div>
  <h2>Growing today.<br>Sustaining tomorrow.</h2>
  <p class="copy">We are committed to environmental stewardship, empowering farmers and building stronger communities.</p>
  <a class="btn btn-ghost" href="#" style="left:240px;top:186px;width:181px;height:34px;border:none;font-size:11.6px">Our Sustainability Journey</a>
  <div class="pillar" style="left:572px"><div class="ring"><svg width="34" height="34" viewBox="0 0 34 34" fill="none" stroke="#ffffff" stroke-width="1.3"><circle cx="17" cy="17" r="12"/><path d="M7 13 C12 14 13 10 17 11 C20 12 19 16 23 16 M10 24 C13 21 16 23 18 20 C21 18 24 21 27 20"/></svg></div>Environmental<br>Impact</div>
  <div class="pillar" style="left:680px"><div class="ring"><svg width="34" height="34" viewBox="0 0 34 34" fill="none" stroke="#ffffff" stroke-width="1.3"><path d="M17 24 V10 M17 14 C13 14 12 11 12 9 C15 9 17 11 17 14 M17 17 C21 17 22 14 22 12 C19 12 17 14 17 17"/><path d="M6 20 L11 26 H23 L28 20 M9 28 H25"/></svg></div>Farmer<br>Empowerment</div>
  <div class="pillar" style="left:788px"><div class="ring"><svg width="34" height="34" viewBox="0 0 34 34" fill="none" stroke="#ffffff" stroke-width="1.3"><circle cx="17" cy="11" r="3.5"/><circle cx="9" cy="14" r="3"/><circle cx="25" cy="14" r="3"/><path d="M11 26 C11 20 23 20 23 26 M4 26 C4 21 12 20 13 22 M30 26 C30 21 22 20 21 22"/></svg></div>Community<br>Development</div>
</section>

<section class="teasers">
  <article class="teaser" style="left:150px">
    <svg class="abs" style="left:108px;top:8px" width="180" height="170" viewBox="0 0 180 170">
      <rect x="20" y="120" width="20" height="40" fill="#4fa323"/>
      <rect x="50" y="100" width="20" height="60" fill="#4fa323"/>
      <rect x="80" y="78" width="20" height="82" fill="#4fa323"/>
      <rect x="110" y="56" width="20" height="104" fill="#4fa323"/>
      <rect x="140" y="34" width="22" height="126" fill="#4fa323"/>
      <path d="M0 104 L40 92 L70 66 L100 74 L150 16" fill="none" stroke="#2c7d1b" stroke-width="3"/>
      <path d="M140 14 L154 10 L152 24 Z" fill="#2c7d1b"/>
      <path d="M10 162 H172" stroke="#cfd3cb"/>
    </svg>
    <div class="body"><div class="eyebrow">Investors</div><h3>Sustainable growth. Strong future.</h3><p>Explore our strategy and performance.</p></div>
    <span class="arrow-btn"><svg width="14" height="10" viewBox="0 0 14 10" fill="none" stroke="#111" stroke-width="1.3"><path d="M1 5 H12 M8 1 L12 5 L8 9"/></svg></span>
  </article>
  <article class="teaser" style="left:454px">
    <div class="teaser-photo" style="background:linear-gradient(90deg,rgba(255,255,255,1) 0%,#b9bcb8 45%,#2a2d2c 100%)" role="img" aria-label="Hand holding a news microphone"></div>
    <div class="body"><div class="eyebrow">News &amp; Media</div><h3>Stay updated with Tallvo.</h3><p>Latest news, stories and events.</p></div>
    <span class="arrow-btn"><svg width="14" height="10" viewBox="0 0 14 10" fill="none" stroke="#111" stroke-width="1.3"><path d="M1 5 H12 M8 1 L12 5 L8 9"/></svg></span>
  </article>
  <article class="teaser" style="left:759px">
    <div class="teaser-photo" style="background:linear-gradient(90deg,rgba(255,255,255,1) 0%,#6f9a55 45%,#235d1c 100%)" role="img" aria-label="Smiling team members in green branded uniforms"></div>
    <div class="body"><div class="eyebrow">Careers</div><h3>Grow your career with us.</h3><p>Be part of a purpose driven team.</p></div>
    <span class="arrow-btn"><svg width="14" height="10" viewBox="0 0 14 10" fill="none" stroke="#111" stroke-width="1.3"><path d="M1 5 H12 M8 1 L12 5 L8 9"/></svg></span>
  </article>
</section>

<footer class="site-footer">
  <div class="footer-brand">tallvo</div>
  <div class="socials"><span aria-label="Social profile"></span><span aria-label="Social profile"></span><span aria-label="Social profile"></span></div>
  <div class="footer-links"><a href="#">Home</a><i>|</i><a href="#">About Us</a><i>|</i><a href="#">Our Services</a><i>|</i><a href="#">How We Help Resources</a><i>|</i><a href="#">Contact Us</a></div>
  <div class="footer-rule"></div>
  <div class="copyright">Copyright © 2026 Tallvo. All rights reserved.</div>
</footer>

</body>
</html>
```